Business Card Design for Photographer

Updating business card design. Must use included logo. We're a luxury wedding photography business. Elegancy, luxury, consistency are messages we wish to convey.

Visit our website at www.colvanderose.com to familiarize yourself more with our brand design currently (fonts, colors etc.). This is what we want to maintain.

Target Market(s)

Luxury Brides and Grooms

Industry/Entity Type

Wedding

Contact Information for Business Card

Current logo (attached to brief)
Name: Colin Vanderose
Phone: 5871302948
website/blog
Email

Requirements
Must have
• Current logo (attached to brief)
• Name: Colin Vanderose
• Phone: 5871302948
• website/blog
• Email
• Instagram username
Should not have
• bright colors, fonts that don't suit our brand (visit www.colvanderose.com)

```html
<!DOCTYPE html>
<html lang="en">
<head>
<meta charset="utf-8">
<title>Colin Vanderose Photographers — Business Card</title>
<link href="https://fonts.googleapis.com/css2?family=Tenor+Sans&family=Open+Sans:wght@400&family=Allura&display=swap" rel="stylesheet">
<style>
  :root {
    --backdrop: #e6e6e6;
    --card: #5e6062;
    --card-edge: #53555a;
    --ink-light: #f4f4f4;
    --ink-soft: #d9dadb;
    --tab: #f7f7f7;
    --ink-dark: #55575a;
  }
  * { margin: 0; padding: 0; box-sizing: border-box; }
  html, body { width: 1200px; height: 852px; overflow: hidden; }
  body {
    background: var(--backdrop);
    display: flex;
    align-items: center;
    justify-content: center;
    gap: 40px;
  }
  .card {
    position: relative;
    width: 540px;
    height: 310px;
    border-radius: 14px;
    background: var(--card);
    box-shadow: 0 2px 0 var(--card-edge), 0 10px 24px rgba(0,0,0,0.18);
    overflow: hidden;
    color: var(--ink-light);
  }
  .wordmark {
    display: flex;
    align-items: center;
    gap: 14px;
    font-family: "Tenor Sans", sans-serif;
    font-weight: 400;
    color: var(--ink-light);
    text-transform: uppercase;
  }
  .wordmark__square {
    width: 38px; height: 38px;
    background: var(--ink-light);
    flex: none;
  }
  .wordmark__name { font-size: 25px; letter-spacing: 0.16em; line-height: 1.1; }
  .wordmark__sub { font-size: 11px; letter-spacing: 0.42em; line-height: 1.6; display: block; }

  .card--front .wordmark {
    position: absolute;
    left: 50%; top: 50%;
    transform: translate(-50%, -50%);
  }

  .card--back .wordmark {
    position: absolute;
    left: 205px; top: 62px;
    gap: 10px;
  }
  .card--back .wordmark__square { width: 30px; height: 30px; }
  .card--back .wordmark__name { font-size: 17px; }
  .card--back .wordmark__sub { font-size: 8px; }

  .name-tab {
    position: absolute;
    left: 0; top: 168px;
    width: 258px; height: 46px;
    background: var(--tab);
    border-radius: 0 14px 0 0;
    display: flex;
    align-items: center;
    padding-left: 30px;
  }
  .name-tab__name {
    font-family: "Allura", cursive;
    font-size: 31px;
    color: var(--ink-dark);
  }
  .contact {
    position: absolute;
    left: 26px; top: 228px;
    list-style: none;
    font-family: "Open Sans", sans-serif;
    font-size: 11px;
    color: var(--ink-soft);
  }
  .contact li { display: flex; align-items: center; gap: 10px; height: 17px; }
  .contact svg { width: 10px; height: 10px; fill: var(--ink-soft); flex: none; }
  .social {
    position: absolute;
    right: 28px; top: 143px;
    display: flex; align-items: center; gap: 7px;
    font-family: "Open Sans", sans-serif;
    font-size: 11px;
    color: var(--ink-soft);
  }
  .social__dot { width: 9px; height: 9px; border-radius: 50%; background: var(--ink-soft); }
</style>
</head>
<body>
  <section class="card card--front" aria-label="Card front">
    <div class="wordmark">
      <span class="wordmark__square" aria-hidden="true"></span>
      <div>
        <span class="wordmark__name">Colin Vanderose</span>
        <span class="wordmark__sub">Photographers</span>
      </div>
    </div>
  </section>

  <section class="card card--back" aria-label="Card back">
    <div class="wordmark">
      <span class="wordmark__square" aria-hidden="true"></span>
      <div>
        <span class="wordmark__name">Colin Vanderose</span>
        <span class="wordmark__sub">Photographers</span>
      </div>
    </div>

    <div class="social">
      <span class="social__dot" aria-hidden="true"></span>
      <span>/colvanderosephoto</span>
    </div>

    <div class="name-tab">
      <span class="name-tab__name">Colin Vanderose</span>
    </div>

    <ul class="contact">
      <li>
        <svg viewBox="0 0 10 10" aria-hidden="true"><path d="M1 3.5C1 2 2 1 3 1h4c1 0 2 1 2 2.5L7.5 4 7 3H3L2.5 4zM2.5 5h5l.5 4h-6z"/></svg>
        <span>(587) 130-2948</span>
      </li>
      <li>
        <svg viewBox="0 0 10 10" aria-hidden="true"><path d="M5 0a5 5 0 1 0 0 10A5 5 0 0 0 5 0zm0 1c.6 0 1.3 1.2 1.5 3h-3C3.7 2.2 4.4 1 5 1zM1.1 6h1.9c.1.9.3 1.7.6 2.3A4 4 0 0 1 1.1 6zm0-2A4 4 0 0 1 3.6 1.7C3.3 2.3 3.1 3.1 3 4zm2.4 2h3c-.2 1.8-.9 3-1.5 3S3.7 7.8 3.5 6zM7 4c-.1-.9-.3-1.7-.6-2.3A4 4 0 0 1 8.9 4zm0 2h1.9a4 4 0 0 1-2.5 2.3C6.7 7.7 6.9 6.9 7 6z"/></svg>
        <span>www.colvanderose.com</span>
      </li>
      <li>
        <svg viewBox="0 0 10 10" aria-hidden="true"><path d="M0 2h10v6H0zm1 1v.3l4 2.5 4-2.5V3z"/></svg>
        <span>colin@colvanderose.com</span>
      </li>
    </ul>
  </section>
</body>
</html>
```